Ford Transit Wrap- Pool Service Company

Looking for full vehicle wrap and half vehicle wrap designs for my swimming pool service and repair company Wren Lagoons LLC. Had a logo designed on here which came out great so hoping for an awesome van wrap too. I want it to have my logo in the design as well as something to do with pools and water, so you can instantly tell it is a swimming pool company at a quick glance. Plus the company information listed. This is a relatively new company so at the moment we only specialize in Pool Service and Repair, Pool Inspections, and Pool Safety Covers. I would like the design to be made so it does not focus on just listing the services allowing it to last many years as our services expand. I have attached a copy of my logo. Please let me know if anything else is needed. This will be going on a Ford Transit 250 148" Medium roof van.
Target Market(s)
high income pool owners
Requirements
Must have
- Logo
Swimming pool look and feel
Pool Service and Repair, Pool Inspections, Safety Covers ...AND MORE!
555-814-2960
www.WrenLagoonsVA.example
Nice to have
- Something very eye catching that grabs attention. Should be able to easily read everything without a lot of clutter or clash.

```html
<!DOCTYPE html>
<html lang="en">
<head>
<meta charset="utf-8">
<title>Wren Lagoons LLC – Van Wrap Sides</title>
<link href="https://fonts.googleapis.com/css2?family=Bebas+Neue&family=Montserrat:wght@400;800&display=swap" rel="stylesheet">
<style>
  :root {
    --navy: #0d3d73;
    --blue: #135a9c;
    --orange: #e05a1c;
    --white: #f4f5f6;
    --url: #d4dfeb;
    --bg: #ffffff;
  }
  html, body {
    margin: 0;
    width: 1199px;
    height: 1200px;
    overflow: hidden;
    background: var(--bg);
  }
  .canvas { position: relative; width: 1199px; height: 1200px; }
  .wrap-side {
    position: absolute;
    left: 50px;
    width: 1100px;
    height: 460px;
    border-radius: 26px;
    overflow: hidden;
    box-shadow: 0 8px 24px rgba(0,0,0,.12);
  }
  .wrap-side.driver { top: 80px; }
  .wrap-side.passenger { top: 660px; }
  .wrap-art { position: absolute; inset: 0; width: 100%; height: 100%; }
  .passenger .wrap-art { transform: scaleX(-1); }

  .brand-dot {
    position: absolute;
    top: 30px;
    width: 120px; height: 120px;
    border-radius: 50%;
    border: 6px solid var(--blue);
    box-sizing: border-box;
  }
  .brand-name {
    position: absolute;
    top: 162px;
    width: 520px;
    margin: 0;
    text-align: center;
    font-family: "Montserrat", sans-serif;
    font-weight: 800;
    font-size: 52px;
    line-height: 1.2;
    letter-spacing: 1px;
    color: var(--navy);
    white-space: nowrap;
  }
  .phone {
    position: absolute;
    top: 312px;
    width: 400px;
    text-align: center;
    font-family: "Montserrat", sans-serif;
    font-weight: 800;
    font-size: 48px;
    line-height: 1.2;
    color: var(--orange);
    white-space: nowrap;
  }
  .web {
    position: absolute;
    top: 380px;
    width: 400px;
    text-align: center;
    font-family: "Montserrat", sans-serif;
    font-weight: 400;
    font-size: 22px;
    line-height: 1.2;
    color: var(--url);
    white-space: nowrap;
  }
  .services {
    position: absolute;
    top: 236px;
    margin: 0;
    padding: 0;
    list-style: none;
    font-family: "Bebas Neue", sans-serif;
    font-size: 25px;
    line-height: 1.05;
    color: var(--white);
    white-space: nowrap;
  }

  .driver .brand-dot { left: 455px; }
  .driver .brand-name { left: 255px; }
  .driver .phone { left: 315px; }
  .driver .web { left: 315px; }
  .driver .services { left: 860px; transform-origin: 0 0; transform: rotate(-25deg); }
  .driver .services li::before { content: "• "; }

  .passenger .brand-dot { left: 525px; }
  .passenger .brand-name { left: 325px; }
  .passenger .phone { left: 385px; }
  .passenger .web { left: 385px; }
  .passenger .services { right: 860px; text-align: right; transform-origin: 100% 0; transform: rotate(25deg); }
  .passenger .services li::after { content: " •"; }
</style>
</head>
<body>
<div class="canvas">

  <section class="wrap-side driver">
    <svg class="wrap-art" viewBox="0 0 1100 460" preserveAspectRatio="none" aria-hidden="true">
      <defs>
        <linearGradient id="blueFillA" x1="0" y1="0" x2="0" y2="1">
          <stop offset="0" stop-color="#135a9c"/>
          <stop offset="1" stop-color="#0b4a88"/>
        </linearGradient>
      </defs>
      <rect width="1100" height="460" fill="#f4f5f6"/>
      <path d="M190 460 C260 370 300 300 400 300 L750 300 C795 300 815 280 825 245 L890 0 L1100 0 L1100 460 Z" fill="url(#blueFillA)"/>
      <path d="M120 460 C200 360 240 270 340 270 L720 270 C760 270 778 255 788 225 L850 0" fill="none" stroke="#c04a1a" stroke-width="14"/>
    </svg>
    <span class="brand-dot"></span>
    <h1 class="brand-name">WREN LAGOONS</h1>
    <ul class="services">
      <li>Pool Service and Repair</li>
      <li>Pool Inspections</li>
      <li>Safety Covers</li>
      <li>And More!</li>
    </ul>
    <div class="phone">555-814-2960</div>
    <div class="web">www.WrenLagoonsVA.example</div>
  </section>

  <section class="wrap-side passenger">
    <svg class="wrap-art" viewBox="0 0 1100 460" preserveAspectRatio="none" aria-hidden="true">
      <defs>
        <linearGradient id="blueFillB" x1="0" y1="0" x2="0" y2="1">
          <stop offset="0" stop-color="#135a9c"/>
          <stop offset="1" stop-color="#0b4a88"/>
        </linearGradient>
      </defs>
      <rect width="1100" height="460" fill="#f4f5f6"/>
      <path d="M190 460 C260 370 300 300 400 300 L750 300 C795 300 815 280 825 245 L890 0 L1100 0 L1100 460 Z" fill="url(#blueFillB)"/>
      <path d="M120 460 C200 360 240 270 340 270 L720 270 C760 270 778 255 788 225 L850 0" fill="none" stroke="#c04a1a" stroke-width="14"/>
    </svg>
    <span class="brand-dot"></span>
    <h2 class="brand-name">WREN LAGOONS</h2>
    <ul class="services">
      <li>Pool Service and Repair</li>
      <li>Pool Inspections</li>
      <li>Safety Covers</li>
      <li>And More!</li>
    </ul>
    <div class="phone">555-814-2960</div>
    <div class="web">www.WrenLagoonsVA.example</div>
  </section>

</div>
</body>
</html>
```